Flyer Design Project for Electricity Demand Response Service

Brindle Power operates a Demand Response Scheme on the National power grid in Ireland. Essentially we sign up commercial electricity users who have a flexible electricity demand (i.e. can switch plant items off when requested) and commercial electricity users who have back-up generators (i.e. can switch their power generators on when requested). This flexible Demand Reduction Capacity is called on by the national grid when the grid wants to balance power supply & power demand. Our participating sites receive significant standby/capacity payments every month just for being available to reduce demand/switch on generators.

This type of business is well established in many countries (USA, UK, France, Germany) but Brindle Power is the first to launch such a business in the Irish market.

We therefore need a two-sided A4 flyer to deliver the following message:

1) Highlight to readers (typically these will be Facility Managers/engineers/CFO's) that our Demand Side Unit will pay their company money in return for offering short and temporary reductions in electricity demand. It is an income stream for commercial users, with no costs involved - a chance to turn their electrical infrastructure from 'cost centres' into 'revenue centres'.

2) Briefly explain to readers what a Demand Side Unit is (prob by using a graphic similar to the graphic we already use in our existing flyer (available for download at www.brindlepower.ie)

3) Highlight two sample 'Case Study' examples of what customers can earn under our scheme

4) Communicate that Brindle Power is licenced by the national regulatory authorities

For examples of how companies promote this business in other countries see www.voltaruze.com, www.dapplegrid.com and www.quorvantix.com

We have already used a flyer during our launch stage and now wish to have a new flyer designed to assist in marketing.

NB! The service we offer is sold to professionals only, mostly in large industrial companies, so it is important that the flyer presents a professional, engineering-competent image

Target Market(s)

Engineers, Facility Managers, Operations Managers, CFOs

Industry/Entity Type

Electrical

Requirements
Must have
• Graphic explaining what a 'Demand Side Unit' does as many readers will not be familiar with our service. I have attached an example of the graphic which we have used in the old flyer but a new graphic would be very welcome. The old flyer and also the new flyer text files which I have attached are not design directions - I am just attached them so you see the amount and type of text & photos which we are currently considering

```html
<!DOCTYPE html>
<html lang="en">
<head>
<meta charset="utf-8">
<title>Brindle Power – Demand Side Management</title>
<link rel="stylesheet" href="https://fonts.googleapis.com/css2?family=Exo+2:wght@300;400;600;700&family=Open+Sans:wght@400;600&display=swap">
<style>
  :root {
    --page-top: #ffffff;
    --page-bottom: #eef0f2;
    --ink: #2b2b2b;
    --heading-blue: #1f5c8e;
    --navy: #1c3f66;
    --text-blue: #3a8fc8;
    --bar-green: #6cbf5a;
    --bar-green-light: #8ed27c;
    --bar-orange: #f0a040;
    --bar-red: #e2725a;
    --bar-track: #ffffff;
    --bar-border: #b9c4cf;
    --green-word: #3fa83a;
    --box-bg: #f7f8f9;
    --box-border: #c9cfd5;
    --rule: #c5ccd3;
    --contact-bg: #dcebf4;
    --label-band: rgba(20, 28, 36, 0.78);
  }
  * { box-sizing: border-box; margin: 0; padding: 0; }
  html, body { width: 848px; height: 1200px; overflow: hidden; }
  body {
    font-family: "Open Sans", Arial, sans-serif;
    color: var(--ink);
    background: linear-gradient(180deg, var(--page-top), var(--page-bottom));
  }
  .flyer { position: relative; width: 848px; height: 1200px; }

  /* Solution cards */
  .card-photo {
    position: absolute; top: 14px; height: 154px;
    border: 1px solid var(--box-border);
    overflow: hidden;
  }
  .card-photo .label {
    position: absolute; left: 0; right: 0; bottom: 0; height: 42px;
    background: var(--label-band); color: #fff;
    font-family: "Open Sans", Arial, sans-serif; font-size: 19px;
    line-height: 42px; padding-left: 10px;
  }
  .card-photo .label.small { font-size: 15.5px; }
  .photo-genset { left: 10px; width: 271px; background: linear-gradient(135deg, #c9d2d8, #8a98a3 55%, #5e6c78); }
  .photo-chillers { left: 291px; width: 265px; background: linear-gradient(135deg, #9aa7a0, #4f8a4a 50%, #3b4a40); }
  .photo-production { left: 567px; width: 269px; background: linear-gradient(180deg, #e6ecf1, #b8c2ca 60%, #8e9aa4); }

  .card-text {
    position: absolute; top: 190px; height: 183px;
    background: var(--box-bg);
    border: 1px solid var(--box-border); border-top: none;
    padding: 8px 12px;
    font-size: 15px; line-height: 21px; text-align: justify;
  }
  .text-genset { left: 10px; width: 271px; }
  .text-chillers { left: 291px; width: 265px; }
  .text-production { left: 567px; width: 269px; }

  .rule { position: absolute; left: 0; width: 848px; height: 1px; background: var(--rule); }

  /* Case studies */
  .case { position: absolute; top: 400px; width: 360px; }
  .case-a { left: 23px; }
  .case-b { left: 468px; text-align: right; }
  .case-title {
    font-family: "Exo 2", Arial, sans-serif; font-weight: 400;
    font-size: 25px; line-height: 28px; color: var(--heading-blue);
  }
  .metric-label {
    position: absolute; font-family: "Exo 2", Arial, sans-serif; font-weight: 700;
    font-size: 18px; color: var(--navy); letter-spacing: 0.3px; white-space: nowrap;
  }
  .case-a .metric-label { left: 0; }
  .case-b .metric-label { right: 0; }
  .bar {
    position: absolute; height: 26px; width: 360px;
    font-family: "Exo 2", Arial, sans-serif; font-weight: 700; font-size: 17px;
    line-height: 26px; color: #fff;
  }
  .bar-green {
    left: 0; background: linear-gradient(180deg, var(--bar-green-light), var(--bar-green));
    border: 1px solid #5aa84a; padding: 0 8px;
    display: flex; justify-content: space-between;
  }
  .bar-track {
    right: 0; background: var(--bar-track); border: 1px solid var(--bar-border);
    display: flex; color: var(--navy);
  }
  .bar-track .fill-orange { margin-left: auto; width: 107px; background: var(--bar-orange); color: #fff; text-align: right; padding-right: 8px; }
  .bar-track .fill-red { width: 66px; background: var(--bar-red); }
  .bar-track .track-text { padding: 0 8px; }
  .bar-track .track-text.end { margin-left: auto; }
  .clocks { position: absolute; display: flex; gap: 4px; }
  .effect-value {
    position: absolute; font-family: "Exo 2", Arial, sans-serif; font-weight: 700; font-size: 18px; white-space: nowrap;
  }
  .case-a .effect-value { left: 0; color: var(--green-word); }
  .case-b .effect-value { right: 0; color: var(--text-blue); }

  /* Load monitoring */
  .monitor-title {
    position: absolute; left: 23px; top: 715px;
    font-family: "Exo 2", Arial, sans-serif; font-weight: 400; font-size: 24px; color: var(--heading-blue);
  }
  .monitor-text {
    position: absolute; left: 23px; top: 754px; width: 806px;
    font-size: 16.5px; line-height: 24px; color: var(--text-blue); text-align: justify;
  }

  /* Credentials */
  .credentials {
    position: absolute; left: 13px; top: 874px; width: 822px; height: 142px;
    border: 1px solid var(--box-border); border-bottom: none; background: rgba(255,255,255,0.5);
    padding: 8px 10px; list-style: none;
    font-size: 15.5px; line-height: 22px; color: #333;
  }
  .credentials li::before { content: "› "; }

  /* Contact */
  .contact {
    position: absolute; left: 13px; top: 1016px; width: 822px; height: 170px;
    background: var(--contact-bg); border: 1px solid var(--box-border);
    padding: 8px 10px; color: var(--text-blue);
  }
  .contact-title { font-family: "Exo 2", Arial, sans-serif; font-size: 18px; font-weight: 400; }
  .contact-intro { font-size: 14px; line-height: 19px; color: var(--text-blue); margin-top: 2px; }
  .contact-cols { display: flex; margin-top: 6px; font-size: 14.5px; line-height: 20px; }
  .contact-col { padding-left: 14px; width: 400px; }
</style>
</head>
<body>
<main class="flyer">

  <section class="solutions">
    <div class="card-photo photo-genset" role="img" aria-label="Photo of onsite back-up generation plant with pipework and pumps"><span class="label">Onsite Back-up Generation</span></div>
    <div class="card-photo photo-chillers" role="img" aria-label="Photo of green chiller and compressor units in a plant room"><span class="label small">Chillers/Compressors/Pumps/etc.</span></div>
    <div class="card-photo photo-production" role="img" aria-label="Photo of rooftop production and cooling equipment"><span class="label">Production Equipment</span></div>

    <p class="card-text text-genset">Sites with back-up generation can switch their energy supply to generation, reducing their grid demand for short periods without affection production</p>
    <p class="card-text text-chillers">By temporarily reducing energy consumption of electrical items such as AC, Compressors, Chillers or Pumps, clients can deliver a flexible demand reduction in return for payments from Brindle Power.</p>
    <p class="card-text text-production">Clients with a flexible production process may chose to temporarily switch off, or re-rate, specific non mission-critical production equipment in order to avail of the Demand Reduction payments.</p>
  </section>

  <div class="rule" style="top:388px"></div>

  <section class="case case-a">
    <h2 class="case-title">CASE STUDY A<br>BACK-UP GENSET</h2>
    <div class="clocks" style="left:277px;top:73px">
      <svg width="30" height="30" viewBox="0 0 30 30"><circle cx="15" cy="15" r="13" fill="#fff" stroke="#7d8790" stroke-width="2"/><path d="M15 6v9l6 4" stroke="#4a545c" stroke-width="1.6" fill="none"/></svg>
      <svg width="30" height="30" viewBox="0 0 30 30"><circle cx="15" cy="15" r="13" fill="#fff" stroke="#7d8790" stroke-width="2"/><path d="M15 6v9l-6 4" stroke="#4a545c" stroke-width="1.6" fill="none"/></svg>
    </div>
    <div class="metric-label" style="top:84px">AVAILABLE CAPACITY</div>
    <div class="bar bar-green" style="top:114px"><span>2000kW</span><span>24 HOURS</span></div>
    <div class="metric-label" style="top:152px">ANNUAL PAYMENTS</div>
    <div class="bar bar-green" style="top:181px"><span>€ 76,000</span></div>
    <div class="metric-label" style="top:224px">EFFECT ON PRODUCTION</div>
    <div class="effect-value" style="top:254px">NONE</div>
  </section>

  <section class="case case-b">
    <h2 class="case-title">CASE STUDY B<br>DIRECT LOAD REDUCTION</h2>
    <div class="clocks" style="left:2px;top:73px">
      <svg width="30" height="30" viewBox="0 0 30 30"><circle cx="15" cy="15" r="13" fill="#fff" stroke="#7d8790" stroke-width="2"/><path d="M15 6v9l-6 4" stroke="#4a545c" stroke-width="1.6" fill="none"/></svg>
    </div>
    <div class="metric-label" style="top:84px">AVAILABLE CAPACITY</div>
    <div class="bar bar-track" style="top:114px"><span class="track-text">7AM - 7PM</span><span class="fill-orange">600 kW</span></div>
    <div class="metric-label" style="top:152px">ANNUAL PAYMENTS</div>
    <div class="bar bar-track" style="top:181px"><span class="track-text end">€ 11,146</span><span class="fill-red"></span></div>
    <div class="metric-label" style="top:224px">EFFECT ON PRODUCTION</div>
    <div class="effect-value" style="top:254px">LIMITED TO 20 EVENTS/YEAR</div>
  </section>

  <div class="rule" style="top:700px"></div>

  <section class="monitoring">
    <h2 class="monitor-title">LOAD MONITORING AND COMMUNICATION</h2>
    <p class="monitor-text">Brindle Power handles all grid interaction via its dedicated dispatch centre. We monitor the load at our customer sites real-time and communicate with our Customers by email, SMS and Phone when a Demand Reduction Event is requested. We can also automate genset start/stop commands if requested by our Customers.</p>
  </section>

  <ul class="credentials">
    <li>Brindle Power is licenced by Commission for Grid Regulation. www.cgr-reg.ie</li>
    <li>Brindle Power is contracted to act as a DSU Aggregator with Gridara www.gridara.com</li>
    <li>Brindle Power is a participant in the Unified Power Market www.upm-o.com.</li>
    <li>The company holds seats on the UPM Trading and Settlement Code Modification Committee and the Grid Code Review Panel</li>
  </ul>

  <section class="contact">
    <h2 class="contact-title">CONTACT BRINDLE POWER NOW TO LEARN MORE:</h2>
    <p class="contact-intro">To allow us assess how your site can avail of Demand Side Mangement and to evaluate the earnings potential of your site, please contact us at:</p>
    <div class="contact-cols">
      <div class="contact-col">Tel: 01 555 0142<br>Email: info@brindlepower.ie<br>Chat: brindlepower<br>www.brindlepower.ie</div>
      <div class="contact-col">Harbourside Enterprise Park,<br>42-46 Quayline Road,<br>Dublin 3</div>
    </div>
  </section>

</main>
</body>
</html>
```